Book cover needed for a major new book on emotional resilience

The book will be titled: 'Storm to Stillness: from rigid habits to pioneers of renewal - The handbook for building steady teams and institutions'
My websites are http://www.brightmarrow.com and http://www.hollenquay.org and I am http://en.pedialoom.org/wiki/Tomas_Brenhurst_(uncertainty_scholar) ad expert in developing emotional resilience. My previous book was The Quiet Compass.
The premise of the book is to introduce brand new material which is the first ever methodology and strategy on how to develop emotional resilience across entire populations like organisations and companies or moving people from fear about change to finding flow through resilience.
The final design should communicate the fact that this is a strategy and methodology. That it is about developing people and entire organisations to be more resilient and who are able to deal with change better.
Target Market(s)
Consultants, Organisational development consultants, Human Resource professionals.

```html
<!DOCTYPE html>
<html lang="en">
<head>
<meta charset="utf-8">
<title>Storm to Stillness — Tomas Brenhurst</title>
<link rel="stylesheet" href="https://fonts.googleapis.com/css2?family=Didact+Gothic&family=Open+Sans:wght@300;400&family=Arimo&display=swap">
<style>
  :root {
    --paper: #ffffff;
    --ink-deep: #0f5a2c;
    --green-main: #1e9a45;
    --green-bright: #1fa85a;
    --teal: #14a88f;
    --badge: #17ad78;
    --badge-ink: #123a22;
    --wing-light: #9ad8b8;
    --wing-deep: #4cb888;
    --larva-light: #2f9a4e;
    --larva-deep: #0f4a26;
    --stair-shadow: #e6e6e6;
  }
  html, body {
    margin: 0;
    padding: 0;
    width: 833px;
    height: 1200px;
    overflow: hidden;
    background: var(--paper);
  }
  .cover {
    position: relative;
    width: 833px;
    height: 1200px;
    background: var(--paper);
    overflow: hidden;
  }
  .cover-art {
    position: absolute;
    inset: 0;
  }
  .author {
    position: absolute;
    left: 21px;
    top: 110px;
    margin: 0;
    font-family: "Didact Gothic", "Century Gothic", sans-serif;
    font-weight: 400;
    font-size: 35px;
    letter-spacing: 0.5px;
    color: var(--ink-deep);
  }
  .title {
    position: absolute;
    left: 20px;
    top: 510px;
    margin: 0;
    font-family: "Open Sans", "Segoe UI", sans-serif;
    font-weight: 400;
    font-size: 67px;
    line-height: 1;
    letter-spacing: 0.5px;
    white-space: nowrap;
    background: linear-gradient(90deg, var(--ink-deep) 0%, var(--green-main) 45%, var(--teal) 100%);
    -webkit-background-clip: text;
    background-clip: text;
    color: transparent;
  }
  .subtitle {
    position: absolute;
    left: 28px;
    top: 608px;
    margin: 0;
    font-family: "Arimo", Arial, sans-serif;
    font-size: 30px;
    color: var(--ink-deep);
    white-space: nowrap;
  }
  .step-label {
    position: absolute;
    margin: 0;
    font-family: "Arimo", Arial, sans-serif;
    font-size: 36px;
    color: var(--green-bright);
  }
  .step-label--one { left: 202px; top: 948px; }
  .step-label--two { left: 340px; top: 831px; }
  .step-label--three { left: 484px; top: 692px; }
  .badge-text {
    position: absolute;
    left: 483px;
    top: 966px;
    width: 328px;
    margin: 0;
    text-align: center;
    font-family: "Open Sans", "Segoe UI", sans-serif;
    font-weight: 300;
    font-size: 18.5px;
    line-height: 32px;
    color: var(--badge-ink);
    text-transform: uppercase;
  }
</style>
</head>
<body>
<main class="cover">
  <svg class="cover-art" width="833" height="1200" viewBox="0 0 833 1200" xmlns="http://www.w3.org/2000/svg">
    <defs>
      <linearGradient id="wing-fill" x1="0" y1="0" x2="1" y2="1">
        <stop offset="0" stop-color="var(--wing-light)"/>
        <stop offset="1" stop-color="var(--wing-deep)"/>
      </linearGradient>
      <linearGradient id="larva-fill" x1="0" y1="0" x2="1" y2="1">
        <stop offset="0" stop-color="var(--larva-light)"/>
        <stop offset="1" stop-color="var(--larva-deep)"/>
      </linearGradient>
      <filter id="badge-shadow" x="-20%" y="-20%" width="140%" height="140%">
        <feDropShadow dx="0" dy="0" stdDeviation="9" flood-color="#000" flood-opacity="0.28"/>
      </filter>
    </defs>

    <path class="frame-corner frame-corner--top" d="M36 3 H712 Q780 3 780 72 V440" fill="none" stroke="var(--green-bright)" stroke-width="2"/>
    <path class="frame-corner frame-corner--bottom" d="M6 1105 V1145 Q6 1173 36 1173 H334" fill="none" stroke="var(--green-bright)" stroke-width="2"/>

    <rect class="butterfly" role="img" aria-label="Illustration of a green butterfly rising above the steps"
          x="520" y="230" width="230" height="245" rx="40" fill="url(#wing-fill)" opacity="0.85"/>

    <g class="staircase">
      <path d="M181 1083 V942 H333 V811 H479 V679 H614" fill="none" stroke="var(--stair-shadow)" stroke-width="14" stroke-linejoin="round"/>
      <path d="M171 1073 V932 H323 V801 H469 V669 H604" fill="none" stroke="var(--green-bright)" stroke-width="3.5" stroke-linejoin="miter"/>
    </g>

    <rect class="caterpillar" role="img" aria-label="Illustration of a caterpillar climbing the first step"
          x="128" y="880" width="132" height="92" rx="30" fill="url(#larva-fill)" opacity="0.85"/>
    <rect class="chrysalis" role="img" aria-label="Illustration of a caterpillar with an emerging butterfly wing on the second step"
          x="274" y="735" width="132" height="108" rx="30" fill="url(#larva-fill)" opacity="0.85"/>

    <circle class="badge" cx="647" cy="1021" r="164" fill="var(--badge)" filter="url(#badge-shadow)"/>
  </svg>

  <p class="author">tomas brenhurst</p>
  <h1 class="title">STORM TO STILLNESS</h1>
  <p class="subtitle">from rigid habits to pioneers of renewal</p>

  <p class="step-label step-label--one">step1</p>
  <p class="step-label step-label--two">step2</p>
  <p class="step-label step-label--three">step3</p>

  <p class="badge-text">The handbook for building<br>steady teams<br>and institutions</p>
</main>
</body>
</html>
```